Dietitian needs awesome business card

I need a contemporary design that's eye catching but professional.
My card is to given to doctors, specialists and patients alike.
I manage patients with chronic diseases
I have uploaded my logo and current business card, I would also like the other Registered Clinical Nutritionist logo incorporated into the design

Target Market(s)

Doctors, specialists and patients

Industry/Entity Type

Healthcare

Contact Information for Business Card

www.brindlecovenutrition.com.au
Ph: 0427 516 903
Fax: 6482 7315
email: marcus.k.wellfare@quorvamail.com
Space on the back of the card with: Appointment date, Appointment time and appointment location

Font styles to use
Serif

Colors
fbee3e
876aae
ffc214

Requirements
Must have
• My Logo
• Registered Clinical Nutritionist Logo
• My 4 locations - Fernhollow Medical Centre, North Kelby Health, Ashcourt Medical, Pinebrook Doctors Surgery
Nice to have
• I like the colours in my current business card

```html
<!DOCTYPE html>
<html lang="en">
<head>
<meta charset="utf-8">
<title>Brindlecove Nutrition &amp; Dietetics – Business Card</title>
<link rel="stylesheet" href="https://fonts.googleapis.com/css2?family=Libre+Baskerville&family=Arimo:wght@400;700&display=swap">
<style>
  :root {
    --backdrop: #2e2f33;
    --card-white: #ffffff;
    --brand-blue: #2336a6;
    --brand-blue-deep: #1a2a8c;
    --brand-blue-light: #2f6fd8;
    --brand-green: #7cc21f;
    --badge-orange: #f07a22;
    --ink: #3b3f7a;
    --rule: #b9bccb;
  }
  * { margin: 0; padding: 0; box-sizing: border-box; }
  html, body { width: 1200px; height: 950px; overflow: hidden; }
  body {
    background: var(--backdrop);
    position: relative;
    font-family: "Arimo", Arial, sans-serif;
  }
  .card {
    position: absolute;
    width: 700px;
    height: 400px;
    background: var(--card-white);
    overflow: hidden;
    box-shadow: 0 10px 30px rgba(0,0,0,.45);
  }
  .card--back { left: 110px; top: 50px; }
  .card--front { left: 390px; top: 500px; }

  .brand {
    position: absolute;
    display: flex;
    align-items: center;
    gap: 12px;
    font-family: "Libre Baskerville", Georgia, serif;
    color: var(--brand-blue);
  }
  .brand__dot {
    width: 44px; height: 44px;
    border-radius: 50%;
    background: var(--brand-blue);
    flex: none;
  }
  .brand__name { line-height: 1.05; }
  .brand__name strong { display: block; font-weight: 400; font-size: 34px; }
  .brand__name span { display: block; font-size: 15px; }
  .card--back .brand { left: 34px; top: 150px; }
  .card--front .brand { left: 40px; top: 220px; }

  /* back: appointment */
  .badge {
    position: absolute; right: 34px; top: 24px;
    width: 124px; height: 52px;
    background: var(--badge-orange);
  }
  .write-line { position: absolute; height: 1px; background: var(--rule); }
  .field-label {
    position: absolute;
    font-size: 17px; color: var(--ink);
  }
  .ampm { position: absolute; right: 40px; top: 94px; font-size: 12px; color: var(--ink); }
  .locations { position: absolute; list-style: none; font-size: 15px; color: var(--ink); }
  .locations li { display: flex; align-items: center; gap: 8px; margin-bottom: 5px; }
  .locations li::before {
    content: ""; width: 12px; height: 12px;
    border: 1.5px solid var(--ink); flex: none;
  }

  /* front */
  .front-art { position: absolute; inset: 0; }
  .holder {
    position: absolute; right: 40px; top: 40px;
    text-align: right; color: #fff;
  }
  .holder__name { font-size: 25px; font-weight: 700; }
  .holder__role { font-size: 15px; font-weight: 700; margin-top: 4px; }
  .contacts {
    position: absolute; right: 34px; top: 190px;
    list-style: none; color: #fff; font-size: 14px; text-align: right;
  }
  .contacts li { display: flex; justify-content: flex-end; align-items: center; gap: 10px; height: 24px; white-space: nowrap; }
  .contacts svg { width: 16px; height: 16px; flex: none; }
</style>
</head>
<body>

<section class="card card--back" aria-label="Appointment card">
  <div class="brand">
    <span class="brand__dot"></span>
    <div class="brand__name"><strong>Brindlecove</strong><span>Nutrition &amp; Dietetics</span></div>
  </div>

  <div class="badge" role="img" aria-label="Registered Clinical Nutritionist badge"></div>

  <span class="ampm">AM/PM</span>
  <div class="write-line" style="left:430px; top:112px; width:230px;"></div>
  <div class="write-line" style="left:430px; top:150px; width:230px;"></div>
  <div class="write-line" style="left:430px; top:188px; width:230px;"></div>

  <span class="field-label" style="left:420px; top:212px;">Time :</span>
  <div class="write-line" style="left:480px; top:230px; width:180px;"></div>
  <ul class="locations" style="left:420px; top:246px;">
    <li>Pinebrook Doctors Surgery</li>
    <li>Ashcourt Medical</li>
  </ul>

  <span class="field-label" style="left:36px; top:290px;">Date :</span>
  <div class="write-line" style="left:96px; top:308px; width:290px;"></div>
  <ul class="locations" style="left:36px; top:322px;">
    <li>Fernhollow Medical Centre</li>
    <li>North Kelby Health</li>
  </ul>
</section>

<section class="card card--front" aria-label="Business card front">
  <svg class="front-art" viewBox="0 0 700 400" preserveAspectRatio="none" aria-hidden="true">
    <defs>
      <radialGradient id="blueGlow" cx="0.72" cy="0.35" r="0.7">
        <stop offset="0" stop-color="#2f6fd8"/>
        <stop offset="0.55" stop-color="#2336a6"/>
        <stop offset="1" stop-color="#1a2a8c"/>
      </radialGradient>
    </defs>
    <rect width="700" height="400" fill="url(#blueGlow)"/>
    <path d="M0,0 H220 C360,60 420,230 380,400 H0 Z" fill="#7cc21f"/>
    <path d="M0,0 H200 C330,40 390,200 345,400 H0 Z" fill="#ffffff"/>
  </svg>

  <div class="brand">
    <span class="brand__dot"></span>
    <div class="brand__name"><strong>Brindlecove</strong><span>Nutrition &amp; Dietetics</span></div>
  </div>

  <div class="holder">
    <div class="holder__name">Marcus Kellaway</div>
    <div class="holder__role">Nutritionist &amp; Chef</div>
  </div>

  <ul class="contacts">
    <li>0427 516 903
      <svg viewBox="0 0 16 16" aria-label="Phone" role="img"><path d="M4 1.5l2.2 3-1.3 1.4a8 8 0 0 0 5.2 5.2l1.4-1.3 3 2.2-1.3 2.3C7.5 14.5 1.5 8.5 1.7 2.8z" fill="#fff"/></svg>
    </li>
    <li>6482 7315
      <svg viewBox="0 0 16 16" aria-label="Fax" role="img"><rect x="4" y="1.5" width="8" height="4" fill="#fff"/><rect x="1.5" y="6" width="13" height="6" rx="1" fill="#fff"/><rect x="4" y="10" width="8" height="4.5" fill="#fff" stroke="#2336a6"/></svg>
    </li>
    <li>marcus.k.wellfare@quorvamail.com
      <svg viewBox="0 0 16 16" aria-label="Email" role="img"><rect x="1.5" y="3.5" width="13" height="9" fill="#fff"/><path d="M1.5 3.5L8 9l6.5-5.5" fill="none" stroke="#2336a6" stroke-width="1.2"/></svg>
    </li>
    <li>www.brindlecovenutrition.com.au
      <svg viewBox="0 0 16 16" aria-label="Website" role="img"><circle cx="8" cy="8" r="6.5" fill="#fff"/><path d="M1.5 8h13M8 1.5c-3 3.5-3 9.5 0 13M8 1.5c3 3.5 3 9.5 0 13" fill="none" stroke="#2336a6" stroke-width="1"/></svg>
    </li>
  </ul>
</section>

</body>
</html>
```